Residential improvers, A Cozy Perch 2 Go *

Cozy Perch 2 Go is a real estate company specializing in turning unloved properties into improved, happy places to live. We specialize in thoughtfully-improved residential properties for buyers or renters. Our company needs a business card that reflects the renovated homes we create using green and Feng Shui principles,

Please disregard the images we submitted. We are looking for an abstract, sophisticated elegant design. No eggs in a nest ... nothing cute. The image can be soft.
Updates

Aloha (hello) all designers. We are a serious property investment/improvement company. We strive to be unique, renovating with style and elegance. Our business card must portray the same message. We thought the nest and flower might be "it" ... clearly it's not, once we saw what you submitted. Please revisit the brief as it was modified yesterday. Mahalo for your input! We look forward to hearing from all designers that have been invited.

Industry/Entity Type

Real Estate Development

Contact Information for Business Card

We will have separate business cards for
1) Corabeth Lindqvist 808-555-0173 corabeth@mailbrook.test
2) Marla Fenwright 808-555-0198 marlafenwright@mailbrook.test
** can we add the website later ... in the process of approval.
Investors * Renovators * Connectors

Font styles to use
Sans Serif

Colors
cadf82

Requirements
Must have
• a feng shui feel ... modern. Color - green with black print.
Nice to have
• A Cozy Perch 2 Go

```html
<!DOCTYPE html>
<html lang="en">
<head>
<meta charset="utf-8">
<title>A Cozy Perch 2 Go – Business Card</title>
<link rel="stylesheet" href="https://fonts.googleapis.com/css2?family=Oswald:wght@400;600&family=Lato:wght@400;700&display=swap">
<style>
  :root {
    --backdrop: #1e1e1e;
    --card: #2d2d2d;
    --green: #cadf82;
    --text-light: #f2f2f2;
    --divider: #e8e8e8;
  }
  html, body {
    margin: 0;
    padding: 0;
    width: 1200px;
    height: 1200px;
    overflow: hidden;
    background: var(--backdrop);
  }
  .canvas {
    position: relative;
    width: 1200px;
    height: 1200px;
  }
  .card {
    position: absolute;
    left: 266px;
    width: 667px;
    height: 380px;
    background: var(--card);
    border-radius: 22px;
  }
  .card--front { top: 198px; }
  .card--back  { top: 628px; }

  /* Front */
  .identity {
    position: absolute;
    right: 354px;
    top: 154px;
    text-align: right;
  }
  .identity__name {
    margin: 0;
    font-family: "Oswald", sans-serif;
    font-size: 29px;
    line-height: 1;
    color: var(--green);
    letter-spacing: 0.5px;
    text-transform: uppercase;
  }
  .identity__first { font-weight: 600; }
  .identity__last  { font-weight: 400; }
  .identity__title {
    margin: 5px 0 0;
    font-family: "Lato", sans-serif;
    font-size: 15px;
    color: var(--text-light);
    letter-spacing: 0.4px;
  }
  .divider {
    position: absolute;
    left: 332px;
    top: 156px;
    width: 1.5px;
    height: 61px;
    background: var(--divider);
  }
  .contact {
    position: absolute;
    left: 349px;
    top: 150px;
    margin: 0;
    padding: 0;
    list-style: none;
    font-family: "Lato", sans-serif;
    font-size: 15.5px;
    color: var(--text-light);
    letter-spacing: 1px;
  }
  .contact__item {
    display: flex;
    align-items: center;
    height: 24.5px;
  }
  .contact__icon {
    width: 11px;
    height: 11px;
    margin-right: 11px;
    flex: none;
  }

  /* Back */
  .brand-name {
    position: absolute;
    left: 0;
    right: 0;
    top: 168px;
    margin: 0;
    text-align: center;
    font-family: "Lato", sans-serif;
    font-weight: 400;
    font-size: 40px;
    letter-spacing: 3px;
    text-transform: uppercase;
    color: var(--green);
  }
  .tagline {
    position: absolute;
    left: 0;
    right: 0;
    top: 325px;
    margin: 0;
    text-align: center;
    font-family: "Lato", sans-serif;
    font-size: 16.5px;
    letter-spacing: 1.6px;
    color: var(--text-light);
  }
  .tagline__dot {
    color: var(--green);
    margin: 0 4px;
  }
</style>
</head>
<body>
<main class="canvas">

  <section class="card card--front" aria-label="Business card front">
    <div class="identity">
      <h1 class="identity__name"><span class="identity__first">Corabeth</span> <span class="identity__last">Lindqvist</span></h1>
      <p class="identity__title">Founder &amp; CEO</p>
    </div>
    <div class="divider"></div>
    <ul class="contact">
      <li class="contact__item">
        <svg class="contact__icon" viewBox="0 0 12 12" aria-hidden="true">
          <path d="M2.6 1 L4.4 1 L5.1 3.6 L3.9 4.6 Q4.9 6.9 7.4 8.1 L8.4 6.9 L11 7.6 L11 9.4 Q11 11 9.4 11 Q1 10.4 1 2.6 Q1 1 2.6 1 Z" fill="var(--green)"/>
        </svg>
        808-555-0173
      </li>
      <li class="contact__item">
        <svg class="contact__icon" viewBox="0 0 12 12" aria-hidden="true">
          <rect x="0.5" y="2.5" width="11" height="8" rx="1" fill="var(--green)"/>
          <path d="M1 3 L6 7 L11 3" fill="none" stroke="var(--card)" stroke-width="1.2"/>
        </svg>
        corabeth@mailbrook.test
      </li>
      <li class="contact__item">
        <svg class="contact__icon" viewBox="0 0 12 12" aria-hidden="true">
          <circle cx="6" cy="6" r="5.5" fill="var(--green)"/>
          <path d="M0.5 6 H11.5 M6 0.5 Q3 6 6 11.5 M6 0.5 Q9 6 6 11.5" fill="none" stroke="var(--card)" stroke-width="0.9"/>
        </svg>
        www.acozyperch2go.test
      </li>
    </ul>
  </section>

  <section class="card card--back" aria-label="Business card back">
    <h2 class="brand-name">A Cozy Perch 2 Go</h2>
    <p class="tagline">INVESTORS<span class="tagline__dot">&bull;</span>RENOVATORS<span class="tagline__dot">&bull;</span>CONNECTORS</p>
  </section>

</main>
</body>
</html>
```